Redesign my business cards

I would like pretty much all the same information as my current business cards but redesigned to stand out more and be more unique photo uploaded to show my current business cards don’t mind if you want to remove or replace I for on the back

```html
<!DOCTYPE html>
<html lang="en">
<head>
<meta charset="utf-8">
<title>Brightline Detailing – Business Card</title>
<link rel="stylesheet" href="https://fonts.googleapis.com/css2?family=Audiowide&family=Roboto:wght@400;700&display=swap">
<style>
  :root {
    --page-bg: #2b2b2c;
    --card-top: #0f3248;
    --card-bottom: #0b2232;
    --accent: #4fa3bf;
    --price: #17a2dc;
    --text-light: #e6ecef;
    --text-soft: #cfd8dd;
    --divider: #1b84b4;
    --logo-tone: #3a4650;
  }
  * { margin: 0; padding: 0; box-sizing: border-box; }
  html, body {
    width: 1200px; height: 1138px; overflow: hidden;
    background: var(--page-bg);
  }
  .card {
    position: absolute;
    left: 275px; width: 622px; height: 375px;
    border-radius: 16px;
    background: radial-gradient(ellipse at 50% 20%, var(--card-top), var(--card-bottom) 75%);
    color: var(--text-light);
    font-family: "Roboto", Arial, sans-serif;
    text-align: center;
    overflow: hidden;
  }
  .card--front { top: 186px; }
  .card--back { top: 608px; }

  .brand {
    position: absolute; left: 0; right: 0; top: 100px;
    display: flex; align-items: center; justify-content: center; gap: 14px;
  }
  .brand__dot {
    width: 30px; height: 30px; border-radius: 50%;
    background: var(--logo-tone);
  }
  .brand__name {
    font-family: "Audiowide", Arial, sans-serif;
    font-size: 26px; color: var(--logo-tone); letter-spacing: 1px;
    background: #5b6a75; -webkit-background-clip: text; background-clip: text;
  }
  .contact__name-line {
    position: absolute; left: 0; right: 0; top: 266px;
    display: flex; justify-content: center; align-items: baseline; gap: 10px;
  }
  .contact__name {
    font-family: "Audiowide", Arial, sans-serif;
    font-size: 25px; color: var(--accent);
  }
  .contact__role { font-size: 20px; color: var(--text-soft); }
  .contact__phone {
    position: absolute; left: 0; right: 0; top: 300px;
    display: flex; justify-content: center; align-items: center; gap: 8px;
    font-size: 23px; font-weight: 700; color: var(--accent); letter-spacing: 0.5px;
  }
  .contact__email {
    position: absolute; left: 0; right: 0; top: 329px;
    display: flex; justify-content: center; align-items: center; gap: 10px;
    font-size: 16px; color: var(--text-soft);
  }

  .back__mark {
    position: absolute; left: 80px; top: -20px;
    width: 460px; height: 440px; border-radius: 50%;
    background: rgba(255,255,255,0.035);
  }
  .service {
    position: absolute; left: 0; right: 0;
  }
  .service__title {
    font-family: "Audiowide", Arial, sans-serif;
    font-size: 20px; color: var(--text-light); letter-spacing: 0.5px;
  }
  .service__price { color: var(--price); }
  .service__desc {
    font-size: 14.5px; line-height: 18px; color: var(--text-soft); margin-top: 3px;
  }
  .divider {
    position: absolute; left: 28px; right: 28px; height: 1px;
    background: linear-gradient(90deg, transparent, var(--divider) 15%, var(--divider) 85%, transparent);
  }
</style>
</head>
<body>
  <section class="card card--front">
    <div class="brand">
      <span class="brand__dot"></span>
      <span class="brand__name">BRIGHTLINE DETAILING</span>
    </div>
    <div class="contact__name-line">
      <span class="contact__name">MASON WHITFIELD</span>
      <span class="contact__role">Owner/Operator</span>
    </div>
    <div class="contact__phone">
      <svg width="24" height="24" viewBox="0 0 24 24" aria-hidden="true">
        <circle cx="12" cy="12" r="10.5" fill="none" stroke="var(--accent)" stroke-width="1.5"/>
        <path d="M8.6 6.8l1.6-.4 1.2 2.6-1.1.9c.6 1.4 1.7 2.5 3.1 3.2l.9-1.1 2.6 1.2-.4 1.6c-.2.6-.8.9-1.4.8-3.4-.6-6-3.2-6.6-6.6-.1-.6.2-1.2.8-1.4z" fill="none" stroke="var(--accent)" stroke-width="1.3"/>
      </svg>
      <span>0412555017</span>
    </div>
    <div class="contact__email">
      <svg width="16" height="12" viewBox="0 0 16 12" aria-hidden="true">
        <rect x="0" y="0" width="16" height="12" fill="var(--accent)"/>
        <path d="M0 0l8 6 8-6" fill="none" stroke="var(--card-bottom)" stroke-width="1.3"/>
      </svg>
      <span>brightlinedetailing@example.com</span>
    </div>
  </section>

  <section class="card card--back">
    <div class="back__mark"></div>

    <div class="service" style="top:50px">
      <h2 class="service__title">INTERIOR DETAIL <span class="service__price">$150</span></h2>
      <p class="service__desc">Vacume &amp; Deep clean of carpets &amp; upholstery or leather treatment, interior trim<br>clean &amp; condition, window polish and treatment, steam clean &amp; stain removal</p>
    </div>
    <div class="divider" style="top:132px"></div>

    <div class="service" style="top:150px">
      <h2 class="service__title">EXTERIOR DETAIL <span class="service__price">$150</span></h2>
      <p class="service__desc">Extreme wash &amp; polish, exterior trim reviver &amp; protector window polish<br>&amp; treatment, tyre dressing, engine bay cleaned</p>
    </div>
    <div class="divider" style="top:231px"></div>

    <div class="service" style="top:249px">
      <h2 class="service__title">FULL EXTREME DETAILS <span class="service__price">$150</span></h2>
      <p class="service__desc">Extreme wash and polish, tyre dressing, engine bay cleaned,<br>vacume &amp; deep clean of carpets &amp; upholstery or leather treatment,<br>interior &amp; exterior trim reviver &amp; protector, window polish and treatment</p>
    </div>
  </section>
</body>
</html>
```